I have a logo I just need a catchy bright flyer.
I offer a fine motor skills program using literacy and numeracy for children aged 4-6.

Tiny Steps Academy is a fun filled learning environment where children can develop their fine motor skills through exploring language, literacy & numeracy.
Special offer: Free trial. (conditions apply)

There is also a website www.tinystepsacademy (Not live as yet)
email address tinystepsacademy@wombanet.com
and phone 0412 530 294

Locations: Glenwood Vale and Ashcombe

```html
<!DOCTYPE html>
<html lang="en">
<head>
<meta charset="utf-8">
<title>Tiny Steps Academy – Fine Motor Skill Development</title>
<link href="https://fonts.googleapis.com/css2?family=Open+Sans:wght@400;700&family=Gochi+Hand&family=Indie+Flower&display=swap" rel="stylesheet">
<style>
  :root {
    --white: #ffffff;
    --navy: #1d3550;
    --purple: #9a4f9e;
    --green-dark: #8cc63f;
    --green-light: #c6de6e;
    --orange: #f6a31f;
    --sky: #cfe7f6;
    --sun: #ffd23a;
  }
  * { margin: 0; padding: 0; box-sizing: border-box; }
  html, body { width: 846px; height: 1200px; overflow: hidden; background: var(--white); }
  .flyer { position: relative; width: 846px; height: 1200px; overflow: hidden; font-family: "Open Sans", sans-serif; }
  .backdrop { position: absolute; inset: 0; }
  .brand { position: absolute; top: 36px; left: 0; width: 792px; text-align: center; }
  .brand-mark { width: 74px; height: 74px; border-radius: 50%; background: var(--sun); margin: 0 auto 40px; }
  .brand-name { font-size: 33px; font-weight: 400; color: var(--navy); line-height: 1.1; }
  .brand-tagline { font-size: 20px; color: var(--navy); margin-top: 10px; }
  .rule { position: absolute; top: 247px; left: 48px; width: 690px; height: 3px;
    background: linear-gradient(90deg, rgba(198,222,110,0), var(--green-light) 20%, var(--green-dark) 60%, rgba(198,222,110,0)); }
  .intro { position: absolute; top: 286px; left: 0; width: 792px; text-align: center;
    font-family: "Gochi Hand", cursive; text-transform: uppercase; color: var(--purple);
    font-size: 34px; letter-spacing: 1.5px; line-height: 60px; }
  .intro span { display: block; }
  .characters { position: absolute; left: 0; top: 598px; width: 770px; height: 230px;
    background: radial-gradient(ellipse at 50% 55%, #e7a86a 0%, #c9b6d8 35%, rgba(160,200,130,0.6) 60%, rgba(207,231,246,0) 80%); opacity: 0.85; }
  .offer { position: absolute; left: 242px; top: 845px; width: 620px; text-align: center;
    font-family: "Indie Flower", cursive; font-size: 48px; line-height: 1; color: var(--white); letter-spacing: 3px;
    transform: rotate(-28deg); transform-origin: center; white-space: nowrap; }
  .contact { position: absolute; top: 1052px; left: 0; width: 860px; text-align: center;
    color: var(--white); font-weight: 700; font-style: normal; font-size: 20px; line-height: 27px; }
</style>
</head>
<body>
<main class="flyer">
  <svg class="backdrop" viewBox="0 0 846 1200" width="846" height="1200" aria-hidden="true">
    <defs>
      <linearGradient id="sky-fade" x1="0" y1="0" x2="0" y2="1">
        <stop offset="0" stop-color="#ffffff"/>
        <stop offset="0.45" stop-color="#e6f3fb"/>
        <stop offset="1" stop-color="#cfe7f6"/>
      </linearGradient>
      <clipPath id="white-field">
        <path d="M0,0 H735 C825,190 830,470 650,700 C500,870 230,870 0,830 Z"/>
      </clipPath>
    </defs>
    <rect width="846" height="1200" fill="var(--green-dark)"/>
    <path d="M0,0 H846 V520 C760,800 380,1010 0,990 Z" fill="var(--green-light)"/>
    <path d="M0,0 H846 V470 C760,700 520,880 250,905 C150,912 60,905 0,890 Z" fill="var(--green-dark)"/>
    <path d="M0,0 H800 C860,260 830,560 620,770 C450,920 200,910 0,880 Z" fill="var(--orange)"/>
    <path d="M0,0 H760 C845,200 840,500 660,720 C500,885 230,885 0,850 Z" fill="var(--green-light)"/>
    <path d="M0,0 H735 C825,190 830,470 650,700 C500,870 230,870 0,830 Z" fill="var(--white)"/>
    <rect x="0" y="540" width="846" height="340" fill="url(#sky-fade)" clip-path="url(#white-field)"/>
  </svg>

  <header class="brand">
    <div class="brand-mark"></div>
    <h1 class="brand-name">Tiny Steps Academy</h1>
    <p class="brand-tagline">Fine Motor Skill Development</p>
  </header>
  <div class="rule"></div>

  <p class="intro">
    <span>Tiny Steps Academy is a fun filled</span>
    <span>learning environment where children</span>
    <span>can develop their fine motor skills</span>
    <span>through exploring language,</span>
    <span>literacy &amp; numeracy.</span>
  </p>

  <div class="characters" role="img" aria-label="Row of friendly cartoon animal characters: elephant, turtle, leopard, monkey, parrot, fox, kangaroo and panda"></div>

  <p class="offer">Special offer: Free trial.</p>

  <address class="contact">
    Glenwood Vale and Ashcombe<br>
    tinystepsacademy@wombanet.com<br>
    phone 0412 530 294<br>
    www.tinystepsacademy
  </address>
</main>
</body>
</html>
```